Kveldbrá - Start-up company selling electricity

Hello let me tell you about Kveldbrá.

Kveldbrá is start-up company selling electricity in Iceland. The operations of the company consist of making power usage forecasts for our customers, purchasing the electricity wholesale from the energy producers, and selling the electricity to the consumer. We are focused on tech by using optimization and machine learning to minimize electricity prices to our customers. Our marketing strategy is to portray a tech company mindset and to show dedication to driving down the electricity price on the market.

We need your help to make our website pop. Possible concepts to work with are as follows:

- Iceland the land of ice and fire
- Green energy
- Innovation
- Tech and data science

Link to our website: https://prufa.kveldbra.is/
We are open to ideas.
Thank you!

Target Market(s)

Electricity consumers both homes and companies.

Number of Pages Required

1 page

Font styles to use
Serif
Sans Serif

```html
<!DOCTYPE html>
<html lang="is">
<head>
<meta charset="utf-8">
<title>Kveldbrá</title>
<link rel="stylesheet" href="https://fonts.googleapis.com/css2?family=Cinzel:wght@400;600;700&family=Mulish:wght@400;500&display=swap">
<style>
:root{
  --navy:#1d2d61;
  --red:#a0302a;
  --ink:#1f1f1f;
  --grey:#efefef;
  --text:#2a2a2a;
  --white:#ffffff;
}
*{margin:0;padding:0;box-sizing:border-box}
html,body{width:1200px;height:999px;overflow:hidden;background:var(--white)}
body{position:relative;font-family:'Mulish',sans-serif;color:var(--text)}
.hero{position:absolute;left:0;top:0;width:1200px;height:460px;
  background:linear-gradient(180deg,#0b3a8a 0%,#1e5fb3 28%,#7c9dbf 45%,#e7c35a 62%,#f2b32b 80%,#c98a24 100%)}
.hero-scene{position:absolute;right:0;top:90px;width:620px;height:370px;
  background:linear-gradient(180deg,rgba(20,40,70,0) 0%,rgba(40,50,50,.25) 60%,rgba(40,60,30,.6) 100%)}
.brand{position:absolute;left:141px;top:28px;display:flex;align-items:center;gap:12px}
.brand-dot{width:32px;height:32px;border-radius:50%;background:var(--white)}
.brand-name{font-family:'Cinzel',serif;font-weight:700;font-size:35px;line-height:44px;color:var(--white);letter-spacing:.5px;text-transform:uppercase}
.nav{position:absolute;top:48px;right:142px;display:flex;gap:26px}
.nav a{font-family:'Cinzel',serif;font-weight:600;font-size:14.5px;color:var(--white);text-decoration:none;letter-spacing:.6px}
.hero-title{position:absolute;left:144px;top:174px;font-family:'Cinzel',serif;font-size:44px;line-height:55px;color:var(--ink);font-weight:400}
.wave{position:absolute;left:0;top:0}
.feature-icon{position:absolute;width:124px;height:124px;margin-left:-62px;margin-top:-62px}
.feature{position:absolute;top:490px;width:300px;margin-left:-150px;text-align:center}
.feature h2{font-family:'Cinzel',serif;font-weight:600;font-size:16.5px;color:var(--ink);letter-spacing:.5px;margin-bottom:14px}
.feature p{font-size:12.6px;line-height:19.2px;color:var(--ink);width:232px;margin:0 auto}
.prices{display:flex;justify-content:center;margin-top:2px}
.price{width:140px;font-size:12.6px;line-height:17px}
.price + .price{border-left:1px solid #d0d0d0}
.price strong{display:block;font-family:Arial,sans-serif;font-weight:400;font-size:20px;margin:4px 0 8px}
.feature p.compare{margin-top:24px;width:auto}
.btn-row{position:absolute;top:648px;display:flex;gap:7px;transform:translateX(-50%)}
.btn{display:inline-block;width:113px;height:39px;line-height:39px;border-radius:20px;text-align:center;
  font-family:'Cinzel',serif;font-weight:600;font-size:13px;color:var(--white);letter-spacing:.6px;background:var(--navy);text-transform:uppercase}
.btn.accent{background:var(--red)}
.footer{position:absolute;left:0;top:760px;width:1200px;height:190px;background:var(--grey)}
.contact{position:absolute;display:flex;gap:14px;align-items:flex-start}
.contact-icon{width:43px;height:43px;border-radius:50%;background:var(--navy);display:flex;align-items:center;justify-content:center;box-shadow:0 0 0 2px #fff inset}
.contact-text{font-size:14.5px;line-height:21px;color:#333}
.contact-text h3{font-family:'Cinzel',serif;font-weight:400;font-size:16px;letter-spacing:.8px;color:#333;margin-bottom:2px;text-transform:uppercase}
.contact-text.small{font-size:12.8px}
.footer-mark{position:absolute;left:569px;top:40px;width:62px;height:62px;border-radius:50%;background:var(--navy)}
.company{position:absolute;left:0;width:1200px;top:132px;text-align:center;font-family:'Cinzel',serif;font-size:14px;line-height:19px;color:#222;letter-spacing:.4px}
.company .sep{margin:0 14px}
.copyright{position:absolute;top:962px;left:0;width:1200px;text-align:center;font-size:12.6px;color:#333}
</style>
</head>
<body>

<header class="hero" role="img" aria-label="Photograph of high-voltage transmission towers against a sunset sky">
  <div class="hero-scene"></div>
</header>

<div class="brand">
  <span class="brand-dot"></span>
  <span class="brand-name">Kveldbrá</span>
</div>

<nav class="nav">
  <a href="#">Viðskiptaskilmálar</a>
  <a href="#">Spurt &amp; Svarað</a>
  <a href="#">Um Kveldbrá</a>
</nav>

<h1 class="hero-title">SAMA RAFMAGN<br>BARA ÓDÝRARA!</h1>

<svg class="wave" width="1200" height="470" viewBox="0 0 1200 470" aria-hidden="true">
  <path d="M0 392 C120 425 250 440 380 442 C520 444 640 425 780 412 C900 402 1030 398 1110 418 C1150 428 1180 442 1200 452 L1200 470 L0 470 Z" fill="#ffffff"/>
  <path d="M0 390 C120 423 250 438 380 440 C520 442 640 423 780 410 C900 400 1030 396 1110 416 C1150 426 1180 440 1200 450" fill="none" stroke="#a0302a" stroke-width="3"/>
</svg>

<svg class="feature-icon" style="left:283px;top:414px" viewBox="0 0 124 124" aria-hidden="true">
  <circle cx="62" cy="62" r="60" fill="none" stroke="#7a86a8" stroke-width="1" stroke-dasharray="2 2"/>
  <circle cx="62" cy="62" r="55" fill="none" stroke="#d6a43a" stroke-width="1"/>
  <circle cx="62" cy="62" r="50" fill="#fff" stroke="#1d2d61" stroke-width="3"/>
  <g fill="none" stroke="#a0302a" stroke-width="2.4" stroke-linecap="round" stroke-linejoin="round">
    <path d="M52 36v10M72 36v10"/>
    <path d="M46 46h32v8a16 16 0 0 1-32 0z"/>
    <path d="M62 70v8c0 6 6 6 8 6"/>
    <path d="M64 51l-4 6h5l-4 6"/>
  </g>
</svg>
<svg class="feature-icon" style="left:596px;top:414px" viewBox="0 0 124 124" aria-hidden="true">
  <circle cx="62" cy="62" r="60" fill="none" stroke="#7a86a8" stroke-width="1" stroke-dasharray="2 2"/>
  <circle cx="62" cy="62" r="55" fill="none" stroke="#d6a43a" stroke-width="1"/>
  <circle cx="62" cy="62" r="50" fill="#fff" stroke="#1d2d61" stroke-width="3"/>
  <g fill="none" stroke="#a0302a" stroke-width="2.2" stroke-linejoin="round">
    <path d="M40 32h36l8 8v52H40z"/>
    <path d="M50 40h8M66 40h8M50 44h8M66 44h8"/>
    <rect x="46" y="52" width="6" height="6"/><path d="M56 55h20"/>
    <rect x="46" y="64" width="6" height="6"/><path d="M56 67h20"/>
    <rect x="46" y="76" width="6" height="6"/><path d="M56 79h20"/>
  </g>
</svg>
<svg class="feature-icon" style="left:918px;top:414px" viewBox="0 0 124 124" aria-hidden="true">
  <circle cx="62" cy="62" r="60" fill="none" stroke="#7a86a8" stroke-width="1" stroke-dasharray="2 2"/>
  <circle cx="62" cy="62" r="55" fill="none" stroke="#d6a43a" stroke-width="1"/>
  <circle cx="62" cy="62" r="50" fill="#fff" stroke="#1d2d61" stroke-width="3"/>
  <path d="M66 32L46 66h14l-6 26 22-36H62z" fill="none" stroke="#a0302a" stroke-width="2.6" stroke-linejoin="round"/>
</svg>

<section class="feature" style="left:283px">
  <h2>Velkomin Í Viðskipti</h2>
  <p>Lorem ipsum dolor sit a consectetuer adipiscing elit, sed diam nonummy nibh euismod tincidunt ut laoreet dolore magna aliquam erat volutpat.Ut wisi enim ad minim veniam quis.</p>
</section>
<div class="btn-row" style="left:283px"><span class="btn">Fyrirtæki</span><span class="btn accent">Heimili</span></div>

<section class="feature" style="left:592px">
  <h2>Verðskrá</h2>
  <div class="prices">
    <div class="price"><strong>6.95</strong>krónur / kWst</div>
    <div class="price"><strong>6.22</strong>krónur / kWst<br>rafmagnskynding</div>
  </div>
  <p class="compare">Gerðu verðsamanburð</p>
</section>
<div class="btn-row" style="left:599px"><span class="btn">Verðvaki</span></div>

<section class="feature" style="left:918px">
  <h2>Framtíðin Er Spennandi</h2>
  <p>Gerum raforkukerfið snallara saman. Kveldbrá notar gervigreind, gagnavísindi og sjálfvirkni til að lágmarka kostnað og stuðla að okrujöfnuði</p>
</section>
<div class="btn-row" style="left:924px;top:647px"><span class="btn">Vita Meira</span></div>

<footer class="footer">
  <div class="contact" style="left:141px;top:36px">
    <span class="contact-icon">
      <svg width="22" height="22" viewBox="0 0 24 24" fill="none" stroke="#fff" stroke-width="1.6" stroke-linejoin="round"><rect x="3" y="6" width="18" height="12" rx="1"/><path d="M3 7l9 6 9-6"/></svg>
    </span>
    <div class="contact-text" style="margin-top:-2px">kveldbra@kveldbra.is<br>555-0199</div>
  </div>
  <div class="contact" style="left:793px;top:36px">
    <span class="contact-icon">
      <svg width="20" height="20" viewBox="0 0 24 24" fill="none" stroke="#fff" stroke-width="1.6"><path d="M12 22s7-7 7-12a7 7 0 0 0-14 0c0 5 7 12 7 12z"/><circle cx="12" cy="10" r="2.5"/></svg>
    </span>
    <div class="contact-text small" style="margin-top:-4px"><h3>Heimilisfang</h3>Lækjarholti 8 210 Garðabæ</div>
  </div>
  <div class="footer-mark"></div>
  <div class="company">Kveldbrá Ehf<br>Kennitala: 510321-0470<span class="sep">·</span>Vskm Númer: 141276</div>
</footer>

<p class="copyright">Copyright © Kveldbrá 2021 Allur Réttur Áskilin</p>

</body>
</html>
```